Fold up small biz card size flyer for Waxing Salon

To design a simple informative flyer which can fold 3 times measuring 2" x 9" for Waxing Salon in Toronto ON CanadaMy client would like both sides of flyer to have text i.e. the first half of flyer text on front and second half with address etc on back.She doesn;t want a company name as yet but would like maybe the simple shape of a body as in this sample deisign with a stone background.the other pics are just samples of ideas she has suggessted and if there is any text it should simply be wax or waxing or maybe body waxing.Please don't hesitate to ask quesition and i look forward to your submissions.

Target Market(s)

women amd men of all adult ages

Font styles to use
Serif
Sans Serif
Decorative
Script

Colors

Designer to choose colors to be used in the design.

Requirements
Must have
• Fold into three to biz card size so PLEASE STRICTLY 2 INCHES X 9 INCHES AND FOLDED DOWN TO A 2 X 3 BIZ CARD
• Due to small size of flyer there will have to be text on back as well
• thanks for your time and patience
Nice to have
• the images are simply ideas of existing brands...just stone background with perhadps small body shaped graphic no company name
Should not have
• scanitly clad women preferably small body shoped graphic only please/

```html
<!DOCTYPE html>
<html lang="en">
<head>
<meta charset="utf-8">
<title>Body Waxing Flyer</title>
<link href="https://fonts.googleapis.com/css2?family=Courgette&family=Montserrat:wght@400;600;700&display=swap" rel="stylesheet">
<style>
:root{
  --bg:#f9e3ee;
  --bg-deep:#eeb6d2;
  --petal:#e48ab5;
  --band:#f3c8dd;
  --pink:#d9267c;
  --pill-border:#e0468f;
  --purple:#7b4aa0;
  --purple-soft:#9a6bb6;
  --panel-border:#eab0cb;
  --ink:#3a2a3a;
  --divider:#d8c6e3;
}
*{margin:0;padding:0;box-sizing:border-box}
html,body{width:1200px;height:5396px;overflow:hidden}
body{position:relative;background:var(--bg);font-family:"Montserrat",sans-serif;color:var(--ink)}
.abs{position:absolute}
.backdrop{left:0;top:0;width:1200px;height:5396px;
  background:
   radial-gradient(ellipse 700px 900px at 1200px 150px,var(--petal) 0%,rgba(228,138,181,0) 70%),
   radial-gradient(ellipse 600px 900px at 0px 1500px,rgba(228,138,181,.8) 0%,rgba(228,138,181,0) 70%),
   radial-gradient(ellipse 700px 900px at 1200px 3900px,rgba(228,138,181,.8) 0%,rgba(228,138,181,0) 70%),
   radial-gradient(ellipse 700px 900px at 0px 5200px,rgba(228,138,181,.7) 0%,rgba(228,138,181,0) 70%),
   var(--bg)}
.offer-band{left:0;top:1780px;width:1200px;height:1774px;background:var(--band)}
.pill{border:3px solid var(--pill-border);border-radius:60px;background:rgba(255,255,255,.35);
  font-family:"Courgette",cursive;color:var(--pink);font-size:78px;display:flex;align-items:center;justify-content:center;white-space:nowrap}
.deal-box{left:222px;top:251px;width:712px;height:1529px;border:2px solid var(--panel-border);background:rgba(255,255,255,.35)}
.deal{left:373px;white-space:nowrap}
.deal h2{font-weight:700;color:var(--purple);font-size:54px;line-height:72px}
.deal h2.big{font-size:66px;line-height:80px}
.deal p{font-size:40px;line-height:72.2px;color:var(--ink)}
.promo-strip{left:4px;top:1939px;width:1196px;height:207px;background:rgba(255,255,255,.55)}
.promo{left:289px;top:1947px;font-weight:700;color:var(--purple-soft);font-size:44px;line-height:62px;white-space:nowrap}
.list-panel{border:2px solid var(--panel-border);background:rgba(255,255,255,.25)}
.list{list-style:none;font-size:38px;line-height:62px;white-space:nowrap}
.list li{position:relative;padding-left:56px}
.list li svg{position:absolute;left:0;top:14px;width:44px;height:36px}
.note{left:718px;top:2855px;font-size:38px;line-height:61.5px;white-space:nowrap}
.note h3{font-weight:700;color:var(--purple-soft);font-size:36px;line-height:62px}
.note p{padding-left:9px}
.fine{left:760px;top:3152px;width:360px;text-align:center;font-size:23px;line-height:62px;font-weight:600;letter-spacing:-.5px}
.fine span{display:block}
.flourish{background:var(--pink);border-radius:50%;opacity:.85}
.contact-box{left:237px;top:3899px;width:714px;height:1051px;border:6px solid var(--panel-border);background:rgba(255,255,255,.45)}
.divider{left:245px;top:4370px;width:699px;height:40px;background:var(--divider)}
.address{left:337px;font-size:44px;line-height:66px;color:var(--purple-soft);white-space:nowrap}
</style>
</head>
<body>
<div class="abs backdrop" role="img" aria-label="Soft pink petal pattern background"></div>
<div class="abs offer-band"></div>

<div class="abs pill" style="left:241px;top:80px;width:716px;height:107px">Door buster Deal !</div>
<div class="abs deal-box"></div>
<div class="abs deal" style="top:263px"><h2>$66 Body Waxing</h2></div>
<div class="abs deal" style="top:341px">
  <p>For women only</p><p>(Neck to Toe -</p><p>Including Brazilian)</p><p>with Take Home Scrub</p><p>used to improve</p><p>in-grown body hair.</p><p>($120 value)</p>
</div>
<div class="abs deal" style="top:904px"><h2 class="big">Guests receive</h2></div>
<div class="abs deal" style="top:988px">
  <p>&nbsp;full body waxing</p><p>during one appointment</p><p>&nbsp;on the following areas:</p><p>&nbsp;butt, hollywood, bikini,</p><p>underarms, stomach,</p><p>cleavage, full back,</p><p>full arms &amp; full legs.</p>
</div>
<div class="abs deal" style="top:1560px"><h2>$66 Body Polishing</h2></div>
<div class="abs deal" style="top:1635px"><p>The secret to soft,</p><p>&nbsp;smooth skin.</p></div>

<div class="abs pill" style="left:230px;top:1803px;width:719px;height:107px">Unbeatable Value !</div>
<div class="abs promo-strip"></div>
<div class="abs promo">Spa Treatments - $13 each<br>when you purchase 5<br>services&nbsp; or more from list below</div>

<svg width="0" height="0" style="position:absolute"><defs><symbol id="tick" viewBox="0 0 44 36"><path d="M4 19 L16 31 L40 5" fill="none" stroke="#e0287e" stroke-width="7" stroke-linecap="round" stroke-linejoin="round"/></symbol></defs></svg>

<div class="abs list-panel" style="left:38px;top:2188px;width:626px;height:1366px"></div>
<ul class="abs list" style="left:63px;top:2201px">
  <li><svg><use href="#tick"/></svg>Back Massage</li>
  <li><svg><use href="#tick"/></svg>Back Scrub</li>
  <li><svg><use href="#tick"/></svg>Spa Manicure</li>
  <li><svg><use href="#tick"/></svg>Full Brazilian Wax</li>
  <li><svg><use href="#tick"/></svg>Full 60 Minute Facial</li>
  <li><svg><use href="#tick"/></svg>Face Polishing</li>
  <li><svg><use href="#tick"/></svg>Face Bleaching</li>
  <li><svg><use href="#tick"/></svg>Scalp &amp; Hair Oil Massage</li>
  <li><svg><use href="#tick"/></svg>Dry Hair Treatment</li>
  <li><svg><use href="#tick"/></svg>Hair Colour Application</li>
  <li><svg><use href="#tick"/></svg>Four Inch Henna Tattoo</li>
  <li><svg><use href="#tick"/></svg>Eyebrow Tinting/Shaping</li>
  <li><svg><use href="#tick"/></svg>Upper Lip Thread/wax</li>
  <li><svg><use href="#tick"/></svg>Forehead Thread/wax</li>
  <li><svg><use href="#tick"/></svg>Side Burn Thread/Wax</li>
  <li><svg><use href="#tick"/></svg>Full Face Thread/Wax</li>
  <li><svg><use href="#tick"/></svg>Nostril Wax</li>
  <li><svg><use href="#tick"/></svg>Nape Wax</li>
  <li><svg><use href="#tick"/></svg>Cleavage Wax</li>
  <li><svg><use href="#tick"/></svg>Stomach Wax</li>
  <li><svg><use href="#tick"/></svg>Upper Back Wax</li>
</ul>

<div class="abs list-panel" style="left:664px;top:2188px;width:494px;height:634px"></div>
<ul class="abs list" style="left:674px;top:2226px">
  <li><svg><use href="#tick"/></svg>Lower Back Wax</li>
  <li><svg><use href="#tick"/></svg>Underarm Wax</li>
  <li><svg><use href="#tick"/></svg>Half Arm Wax</li>
  <li><svg><use href="#tick"/></svg>Full Arm Wax</li>
  <li><svg><use href="#tick"/></svg>Half Legs Wax</li>
  <li><svg><use href="#tick"/></svg>Full Legs Wax</li>
  <li><svg><use href="#tick"/></svg>Bikini Line Wax</li>
  <li><svg><use href="#tick"/></svg>Bum Wax</li>
  <li><svg><use href="#tick"/></svg>Hollywood Wax</li>
</ul>

<div class="abs note">
  <h3>Note</h3>
  <p>$5 extra for nail polish</p>
  <p>counts as 2 services</p>
  <p>counts as 3 services</p>
</div>
<div class="abs flourish" style="left:706px;top:3134px;width:64px;height:66px" role="img" aria-label="Decorative flourish"></div>
<div class="abs fine">
  <span>Services may be</span>
  <span>Shared with your</span>
  <span>Loved Ones</span>
  <span>Some conditions apply</span>
</div>
<div class="abs flourish" style="left:1066px;top:3334px;width:66px;height:76px" role="img" aria-label="Decorative flourish"></div>

<div class="abs pill" style="left:195px;top:3707px;width:812px;height:108px">Call today to book a spot.</div>
<div class="abs contact-box"></div>
<div class="abs divider"></div>
<div class="abs address" style="top:3927px">
  742 MAPLEWOOD ST EAST<br>#3&nbsp; Toronto<br>ON&nbsp; M4X 0A1<br>Opp to Saffron Grill House<br>(416) 555-0142<br>1 (833) 555-0118
</div>
<div class="abs address" style="top:4452px">
  2210 Birchmount Park Ave,<br>#3.&nbsp; North York,<br>ON&nbsp; M4X 0B2<br>Opp to Harbour Mall<br>Next to Ridgeway Rentals<br>(416) 555-0176.<br>1 (833) 555-0193
</div>
</body>
</html>
```